Tidewell show guide

I need to design a one page 7x10 pdf that will be printed. It will include our logo and the following text:

#1 Disaster Mitigation Lead Platform

We generated over 60 million in
revenue last year fo our contractors.

Leads types:
-Water Damage
-Fire Damage
-Mold Remediation
-Biohazard
-Plumbing
-Carpet Cleaning

Exclusive leads
No monthly fees
Only pay for valid leads

Stop by booth 527 to get to your cut!

Target Market(s)

Home service contractors

Colors
9bcb3b
0255a3

Requirements
Must have
• our logo and text
Should not have
• any clutter

```html
<!DOCTYPE html>
<html lang="en">
<head>
<meta charset="utf-8">
<title>Ridgeway Leads – Show Guide</title>
<link href="https://fonts.googleapis.com/css2?family=Open+Sans:wght@300;400;600;700;800&display=swap" rel="stylesheet">
<style>
  :root {
    --blue: #3a7fdf;
    --blue-deep: #2f6fd6;
    --green: #1aa33f;
    --green-mid: #1f9a5a;
    --ink: #1f1f1f;
    --pill: #222222;
    --tile: #f4f4f4;
    --tile-edge: #e6e6e6;
    --icon-spot: #dcdcdc;
    --paper: #ffffff;
    --text: #333333;
  }
  * { box-sizing: border-box; margin: 0; padding: 0; }
  html, body { width: 800px; height: 1200px; overflow: hidden; background: var(--paper); }
  body { font-family: "Open Sans", Arial, sans-serif; color: var(--text); }
  .page { position: relative; width: 800px; height: 1200px; background: var(--paper); overflow: hidden; }

  .header-band {
    position: absolute; left: 0; top: 0; width: 800px; height: 267px;
    background: linear-gradient(90deg, var(--blue) 0%, #2a8aa8 45%, var(--green) 100%);
  }
  .header-art {
    position: absolute; left: 95px; top: 65px; width: 175px; height: 160px;
    border-radius: 10px;
    background: linear-gradient(180deg, rgba(255,255,255,0.18), rgba(255,255,255,0.06));
  }
  .brand-pill {
    position: absolute; left: 305px; top: 68px; width: 495px; height: 141px;
    background: var(--paper); border-radius: 71px 0 0 71px;
    display: flex; align-items: center; padding-left: 52px;
  }
  .brand-name { font-weight: 700; font-size: 34px; color: var(--green); }

  .divider { position: absolute; left: 152px; top: 276px; width: 471px; height: 1px; background: var(--green); }
  .divider-accent { position: absolute; left: 334px; top: 275px; width: 106px; height: 3px; background: var(--blue-deep); }

  .headline { position: absolute; left: 0; top: 308px; width: 800px; text-align: center; color: var(--blue-deep); }
  .headline-light { display: block; font-weight: 300; font-size: 48px; line-height: 56px; letter-spacing: -1px; }
  .headline-bold { display: block; font-weight: 700; font-size: 49px; line-height: 58px; letter-spacing: -1px; }

  .stat { position: absolute; left: 251px; top: 464px; display: flex; align-items: center; }
  .stat-seal {
    width: 90px; height: 90px; border-radius: 50%;
    background: radial-gradient(circle, #ffffff 0 38%, #f2a93b 39% 52%, #1a9a3c 53% 100%);
  }
  .stat-rule { width: 2px; height: 40px; background: var(--blue-deep); margin: 0 22px 0 22px; }
  .stat-text { font-size: 15.5px; line-height: 21px; color: var(--text); }
  .stat-figure { display: block; font-weight: 700; font-size: 25px; line-height: 28px; color: var(--ink); }

  .lead-types {
    position: absolute; left: 183px; top: 604px; width: 416px;
    display: grid; grid-template-columns: repeat(3, 128px); grid-auto-rows: 128px; gap: 13px 16px;
  }
  .lead-tile {
    background: var(--tile); border: 1px solid var(--tile-edge); border-radius: 12px;
    display: flex; flex-direction: column; align-items: center; justify-content: center; gap: 14px;
    font-size: 14px; color: var(--text); padding-top: 6px;
  }
  .lead-icon { width: 54px; height: 54px; border-radius: 50%; background: var(--icon-spot); }

  .perks { position: absolute; left: 142px; top: 914px; display: flex; gap: 14px; }
  .perk {
    background: var(--pill); color: #fff; font-weight: 700; font-size: 14px;
    height: 31px; line-height: 31px; padding: 0 16px; border-radius: 16px;
  }

  .cta { position: absolute; left: 0; top: 987px; width: 800px; text-align: center; }
  .cta-main { display: block; font-weight: 700; font-size: 29px; line-height: 34px; letter-spacing: -1.5px; color: var(--blue-deep); }
  .cta-main .booth { color: var(--green-mid); }
  .cta-sub { display: block; font-weight: 400; font-size: 28px; line-height: 32px; letter-spacing: -1.5px; color: var(--blue-deep); }

  .footer-wave { position: absolute; left: 0; bottom: 0; width: 800px; height: 160px; }
</style>
</head>
<body>
<main class="page">
  <header class="header-band">
    <div class="header-art" role="img" aria-label="Faint line drawing of buildings cracked by an earthquake"></div>
    <div class="brand-pill">
      <span class="brand-name">Ridgeway Leads</span>
    </div>
  </header>

  <div class="divider"></div>
  <div class="divider-accent"></div>

  <h1 class="headline">
    <span class="headline-light">Disaster Mitigation</span>
    <span class="headline-bold">Lead Platform</span>
  </h1>

  <section class="stat">
    <div class="stat-seal" role="img" aria-label="Green seal badge with a thumbs-up"></div>
    <div class="stat-rule"></div>
    <p class="stat-text">We generated over<span class="stat-figure">60 million</span>in revenue last year<br>for our contractors.</p>
  </section>

  <section class="lead-types">
    <div class="lead-tile">
      <div class="lead-icon" role="img" aria-label="Water damage icon"></div>
      <span>Water Damage</span>
    </div>
    <div class="lead-tile">
      <div class="lead-icon" role="img" aria-label="Fire damage icon"></div>
      <span>Fire Damage</span>
    </div>
    <div class="lead-tile">
      <div class="lead-icon" role="img" aria-label="Mold remediation icon"></div>
      <span>Mold Remediation</span>
    </div>
    <div class="lead-tile">
      <div class="lead-icon" role="img" aria-label="Biohazard icon"></div>
      <span>Biohazard</span>
    </div>
    <div class="lead-tile">
      <div class="lead-icon" role="img" aria-label="Plumbing icon"></div>
      <span>Plumbing</span>
    </div>
    <div class="lead-tile">
      <div class="lead-icon" role="img" aria-label="Carpet cleaning icon"></div>
      <span>Carpet Cleaning</span>
    </div>
  </section>

  <section class="perks">
    <span class="perk">Exclusive leads</span>
    <span class="perk">No monthly fees</span>
    <span class="perk">Only pay for valid leads</span>
  </section>

  <p class="cta">
    <span class="cta-main">Stop by <span class="booth">booth 527</span></span>
    <span class="cta-sub">to get to your cut!</span>
  </p>

  <svg class="footer-wave" viewBox="0 0 800 160" preserveAspectRatio="none" aria-hidden="true">
    <defs>
      <linearGradient id="waveFill" x1="0" x2="1" y1="0" y2="0">
        <stop offset="0" stop-color="#3a7fdf"/>
        <stop offset="0.5" stop-color="#2a8aa8"/>
        <stop offset="1" stop-color="#1aa33f"/>
      </linearGradient>
    </defs>
    <path d="M0 0 C180 30 330 62 480 68 C620 74 730 66 800 58 L800 160 L0 160 Z" fill="url(#waveFill)"/>
    <path d="M440 66 C610 76 740 60 800 0 L800 58 C730 68 620 78 440 66 Z" fill="#0d0d0d"/>
  </svg>
</main>
</body>
</html>
```